Lumo4Kart - a fintech company - business card

We need a business card design for our Payments Technology company in Sydney, Australia. We provide business with payment solutions expanding across EFTPOS machines, online payment gateways and mobile payment solutions. We would like to see designs that are clean, classy and professional.
Target Market(s)
Business professionals, executives, c-suite
Industry/Entity Type
Fintech
Contact Information for Business Card
Will be on 400gsm. Logo will most likely be spot gloss unless designer recommends otherwise.
Font styles to use
Sans Serif
Requirements
Must have
- We need our website (lumo4kart.com.au), email (contact@lumo4kart.com.au), mobile (0432 587 904) and direct phone number (02 6815 3927) to feature on the card along with our logo (attached) and the words "EFTPOS | ONLINE | MOBILE"
- Font = Roboto

```html
<!DOCTYPE html>
<html lang="en">
<head>
<meta charset="utf-8">
<title>Lumo4Kart – Business Card</title>
<link rel="stylesheet" href="https://fonts.googleapis.com/css2?family=Roboto:wght@400;500;700&display=swap">
<style>
  :root {
    --brand-blue: #126090;
    --ink: #000000;
    --text-dark: #222222;
    --logo-grey: #6b6b6b;
    --mist: #e3edf2;
    --mist-back: #d6e3eb;
    --slate: #8e979d;
    --line-grey: #b3b3b3;
    --paper: #ffffff;
  }
  html, body {
    margin: 0;
    padding: 0;
    width: 1200px;
    height: 1200px;
    overflow: hidden;
    background: var(--paper);
    font-family: "Roboto", sans-serif;
  }
  .sheet { display: block; width: 1200px; height: 1200px; }
  .card-edge { fill: var(--paper); stroke: #222; stroke-width: 3; }
  .fill-blue { fill: var(--brand-blue); }
  .fill-ink { fill: var(--ink); }
  .fill-mist { fill: var(--mist); }
  .fill-mist-back { fill: var(--mist-back); }
  .slate-band { fill: var(--slate); opacity: .75; }
  .slate-line { fill: var(--line-grey); }
  .brand-mark { fill: var(--brand-blue); }
  .brand-name { font-family: "Roboto", sans-serif; font-weight: 700; fill: var(--logo-grey); text-anchor: middle; }
  .site-top { font-family: "Roboto", sans-serif; font-size: 26px; fill: var(--text-dark); }
  .site-top .accent { fill: var(--brand-blue); }
  .services { font-family: "Roboto", sans-serif; font-size: 32px; font-weight: 500; fill: var(--text-dark); }
  .person-name { font-family: "Roboto", sans-serif; font-size: 58px; fill: var(--brand-blue); }
  .person-name .first { font-weight: 700; }
  .person-role { font-family: "Roboto", sans-serif; font-size: 24px; font-weight: 700; fill: var(--logo-grey); }
  .contact { font-family: "Roboto", sans-serif; font-size: 25px; fill: var(--text-dark); }
  .icon-ink { fill: var(--ink); }
  .icon-stroke { fill: none; stroke: var(--ink); stroke-width: 4; stroke-linecap: round; }
  .icon-white { fill: none; stroke: var(--paper); stroke-width: 6; stroke-linejoin: round; }
  .globe-line { fill: none; stroke: var(--paper); stroke-width: 5; }
</style>
</head>
<body>
<svg class="sheet" viewBox="0 0 1500 1500" xmlns="http://www.w3.org/2000/svg">
  <defs>
    <clipPath id="front-clip"><rect x="219" y="82" width="1077" height="615"/></clipPath>
    <clipPath id="back-clip"><rect x="219" y="802" width="1077" height="626"/></clipPath>
  </defs>

  <!-- Front of card -->
  <g class="card-front">
    <rect class="card-edge" x="219" y="82" width="1077" height="615"/>
    <g clip-path="url(#front-clip)">
      <circle class="fill-mist" cx="490" cy="375" r="275"/>
      <path class="fill-blue" d="M219,82 H483 L545,195 Q562,235 520,258 L219,423 Z"/>
      <path class="fill-ink" d="M219,82 H455 L480,130 Q494,165 460,183 L219,312 Z"/>
      <path class="fill-blue" d="M1030,82 H1296 V697 H690 L535,410 Q515,370 555,350 Z"/>
      <path class="fill-ink" d="M1190,82 H1296 V697 H710 L585,455 Q565,420 600,405 Z"/>
    </g>
    <text class="site-top" x="577" y="152">www.<tspan class="accent">lumo4kart</tspan>.com.au</text>
    <circle class="brand-mark" cx="1018" cy="432" r="68"/>
    <text class="brand-name" x="1015" y="582" font-size="64">LUMO4KART</text>
    <text class="services" x="235" y="620">EFTPOS | ONLINE | MOBILE</text>
  </g>

  <!-- Back of card -->
  <g class="card-back">
    <rect class="card-edge" x="219" y="802" width="1077" height="626"/>
    <g clip-path="url(#back-clip)">
      <circle class="fill-mist-back" cx="690" cy="1210" r="330"/>
      <path class="slate-line" d="M797,802 H815 L985,1110 L965,1120 Z"/>
      <path class="slate-band" d="M925,1060 L965,1085 Q992,1130 958,1155 L470,1428 H310 L905,1095 Q932,1082 925,1060 Z"/>
      <path class="fill-blue" d="M1296,1110 V1428 H1050 L990,1320 Q975,1285 1005,1268 Z"/>
      <path class="fill-ink" d="M1296,1215 V1428 H1075 L1052,1385 Q1040,1350 1070,1333 Z"/>
    </g>

    <circle class="brand-mark" cx="1098" cy="910" r="66"/>
    <text class="brand-name" x="1096" y="1046" font-size="60">LUMO4KART</text>

    <text class="person-name" x="370" y="918"><tspan class="first">NAME</tspan> HERE</text>
    <text class="person-role" x="371" y="945">DESIGNATION</text>
    <rect class="fill-ink" x="277" y="959" width="479" height="6"/>

    <!-- phone icon -->
    <g class="icon-phone">
      <path class="icon-ink" d="M272,1048 Q268,1040 280,1036 L290,1034 L305,1058 L294,1066 Q300,1078 312,1084 L322,1074 L338,1088 L334,1094 Q322,1102 306,1094 Q280,1078 272,1048 Z"/>
      <path class="icon-stroke" d="M308,1044 Q320,1046 324,1058"/>
      <path class="icon-stroke" d="M308,1036 Q328,1038 332,1058"/>
      <path class="icon-stroke" d="M308,1028 Q336,1030 340,1058"/>
    </g>
    <text class="contact" x="367" y="1060">0432 587 904</text>
    <text class="contact" x="367" y="1085">02 6815 3927</text>

    <!-- mail icon -->
    <g class="icon-mail">
      <circle class="icon-ink" cx="302" cy="1152" r="40"/>
      <path class="icon-white" d="M281,1170 V1137 L302,1158 L323,1137 V1170"/>
      <rect class="icon-white" x="281" y="1137" width="42" height="33"/>
    </g>
    <text class="contact" x="367" y="1160">contact@lumo4kart.com.au</text>

    <!-- web icon -->
    <g class="icon-web">
      <circle class="icon-ink" cx="302" cy="1241" r="37"/>
      <ellipse class="globe-line" cx="302" cy="1241" rx="14" ry="34"/>
      <line class="globe-line" x1="302" y1="1207" x2="302" y2="1275"/>
      <line class="globe-line" x1="268" y1="1241" x2="336" y2="1241"/>
      <line class="globe-line" x1="274" y1="1224" x2="330" y2="1224"/>
      <line class="globe-line" x1="274" y1="1258" x2="330" y2="1258"/>
    </g>
    <text class="contact" x="367" y="1247">www.lumo4kart.com.au</text>
  </g>
</svg>
</body>
</html>
```